Label for Dog Nourishing CBD Balm

Dear Designers,

We are looking for a packaging expert to design our new Hydrating Balm for dogs which contain a relaxing hemp extract (CBD). The product is intended to be massaged on the dog’s paws to make them softer and promote the animal’s well-being :)

Our company is already selling various relaxing cat & dog products, and we would like this new design to reflect the same "style & feeling" as our current products (see attached ZIP file).

Technical aspects:
- The packaging is a 40ml aluminium jar (58mm x 23mm).
- We are looking to design 2 separate labels (one for the front, one for the back)
- The label dimensions should be : 50mm x 50mm
- Please follow technical guidelines from printer (see ZIP file).

Design aspects:
- The design should be compatible with our brand identity (i.e. fluffly, pure, relaxing, positive, clean & natural).
- People should understand what the product "is" and what the product "does" simply from looking at the design.
- The actual balm is white/yellow in color.
- Soft/rounded shapes are preferred.
- Please use our brand's colors (see typo & colors in ZIP file)
- Please use our brand's fonts (see typo & colors in ZIP file)
- Please use our company logo (see ZIP file).
- The design also needs to convey a strong sense of professionalism as we are an animal "healthcare" brand.
- If you want to include a dog picture, we would prefer you to use a picture of our official brand ambassador (see ZIP file).
- Only original work (no plagiarism will be accepted).

Please don't hesitate to send us a message if you have any questions about the brand, the product or the design requirements.

We look forward to seeing your designs & working on this together !

Thanks & regards,
Marcus

Target Market(s)

Dog owners

Font styles to use
Other font styles liked:
• See ZIP file

Requirements
Must have
• Brand fonts (see typo & colors in ZIP file)
Brand colors (see typo & colors in ZIP file)

```html
<!DOCTYPE html>
<html lang="en">
<head>
<meta charset="utf-8">
<title>VerdaBalm Soothing Balm – Front and Back Labels</title>
<link rel="stylesheet" href="https://fonts.googleapis.com/css2?family=Nunito:wght@800;900&family=Quicksand:wght@500;600;700&display=swap">
<style>
  :root {
    --green: #3a9f80;
    --green-dark: #1d3b2c;
    --orange: #e8700f;
    --label-light: #f6f7f7;
    --label-mid: #e6e8e8;
    --page: #ffffff;
    --photo-light: #eceae8;
    --photo-mid: #d8d3cf;
  }
  * { margin: 0; padding: 0; box-sizing: border-box; }
  html, body { width: 1200px; height: 1200px; overflow: hidden; background: var(--page); }
  body { position: relative; font-family: "Quicksand", sans-serif; }

  .side-title {
    position: absolute; top: 238px; width: 360px; text-align: center;
    font-family: "Nunito", sans-serif; font-weight: 900; font-size: 72px;
    color: var(--green); line-height: 1;
  }
  .side-title--front { left: 140px; }
  .side-title--back { left: 714px; }

  .label {
    position: absolute; top: 419px; width: 450px; height: 450px;
    border-radius: 50%; overflow: hidden;
    background: radial-gradient(circle at 45% 40%, var(--label-light) 0%, var(--label-mid) 100%);
  }
  .label::after {
    content: ""; position: absolute; inset: 0; border-radius: 50%;
    border: 7px solid var(--green); pointer-events: none; z-index: 5;
  }
  .label--front { left: 103px; }
  .label--back { left: 669px; }

  .abs { position: absolute; }
  .center-x { left: 0; width: 100%; text-align: center; }

  /* Front */
  .brand-name {
    top: 70px; font-weight: 700; font-size: 28px; letter-spacing: 1px;
    color: var(--green-dark); line-height: 1;
  }
  .brand-name .dot {
    display: inline-block; width: 12px; height: 12px; border-radius: 50%;
    background: var(--green-dark); margin-right: 8px; vertical-align: 3px;
  }
  .ribbon { left: 66px; top: 131px; width: 318px; height: 59px; }
  .product-name {
    top: 131px; height: 59px; line-height: 59px;
    font-family: "Nunito", sans-serif; font-weight: 900; font-size: 44px; color: #fff;
  }
  .product-type { top: 190px; font-weight: 700; font-size: 28px; color: var(--orange); line-height: 1.2; }
  .strength { top: 238px; font-weight: 600; font-size: 19px; color: var(--green-dark); }
  .strength .cbd { color: var(--green); }
  .benefit-band {
    left: 0; top: 272px; width: 100%; height: 33px; background: var(--green);
    color: #fff; font-weight: 700; font-size: 19px; line-height: 33px; text-align: center;
    word-spacing: 2px;
  }
  .ambassador-photo {
    left: 156px; top: 306px; width: 138px; height: 144px;
    background: radial-gradient(ellipse at 50% 45%, var(--photo-mid) 0%, var(--photo-light) 60%, rgba(236,234,232,0) 100%);
  }
  .spec {
    top: 355px; width: 80px; text-align: center;
    font-weight: 600; font-size: 14px; line-height: 17px; color: var(--green);
  }
  .spec--weight { left: 77px; }
  .spec--thc { left: 294px; }

  /* Back */
  .back-heading { font-weight: 700; font-size: 14px; color: var(--green-dark); line-height: 1; }
  .back-copy {
    left: 100px; width: 250px; text-align: center;
    font-weight: 500; font-size: 11.5px; line-height: 14.5px; color: var(--green);
  }
  .h-relax { top: 50px; }
  .c-relax { top: 66px; }
  .h-use { top: 164px; }
  .c-use { top: 181px; }
  .h-ingr { top: 265px; }
  .c-ingr { top: 281px; }
  .distributor {
    left: 112px; top: 330px; font-weight: 700; font-size: 10px; line-height: 13.5px;
    color: var(--green-dark);
  }
  .distributor .lead { display: block; margin-left: 13px; margin-bottom: 1px; }
  .back-brand {
    left: 226px; top: 362px; width: 100px; text-align: center;
    font-weight: 700; font-size: 16px; color: var(--green-dark); line-height: 1;
  }
  .back-web {
    left: 226px; top: 392px; width: 100px; text-align: center;
    font-weight: 700; font-size: 8px; color: var(--green-dark);
  }
</style>
</head>
<body>
  <h2 class="side-title side-title--front">Front</h2>
  <h2 class="side-title side-title--back">Back</h2>

  <section class="label label--front">
    <div class="abs center-x brand-name"><span class="dot"></span>VERDALIS</div>
    <svg class="abs ribbon" viewBox="0 0 318 59" aria-hidden="true">
      <polygon points="0,0 318,0 293,29.5 318,59 0,59 25,29.5" fill="var(--green)"/>
    </svg>
    <h1 class="abs center-x product-name">VerdaBalm</h1>
    <p class="abs center-x product-type">soothing balm</p>
    <p class="abs center-x strength"><span class="cbd">CBD</span> 250mg</p>
    <p class="abs benefit-band">Repair &nbsp;•&nbsp; Nourish • &nbsp;Protect</p>
    <div class="abs ambassador-photo" role="img" aria-label="Photo of the brand ambassador, a cream-coloured wrinkled puppy"></div>
    <p class="abs spec spec--weight">NET WT:<br>40g</p>
    <p class="abs spec spec--thc">0%<br>THC</p>
  </section>

  <section class="label label--back">
    <h3 class="abs center-x back-heading h-relax">EVERYDAY RELAXATION</h3>
    <p class="abs back-copy c-relax">This balm repairs, nourishes and protects your dog's sensitive skin. Its trusted multi-action formula brings relief to fragile areas and soothes temporary irritations (paw pads, elbows, etc.)</p>
    <h3 class="abs center-x back-heading h-use">RECOMMENDED USE:</h3>
    <p class="abs back-copy c-use">Rub a small amount of balm in the palm of your hand and apply to sensitive areas as a daily care ritual. Repeat until the product has been completely absorbed.</p>
    <h3 class="abs center-x back-heading h-ingr">INGREDIENTS:</h3>
    <p class="abs back-copy c-ingr">Shea Butter, Beeswax, Coconut Oil, Hemp Extract (0% THC).</p>
    <address class="abs distributor" style="font-style:normal">
      <span class="lead">Distributed by:</span>
      VERDA EUROPE KFT.<br>
      Lomb utca 14<br>
      1072 Budapest<br>
      Hungary
    </address>
    <div class="abs back-brand">VERDALIS</div>
    <div class="abs back-web">www.verdalis.co</div>
  </section>
</body>
</html>
```